Heron Provisions
Project: Heron Stationery
Heron Stationery - Food
Heron Stationery
Modern
Faisal Bakrouni
CEO
Phone: 012 4738205 012 4719360 Fax: 012 4782513 487 Jeddah 23857 Sawsan St. Sawsan cross Qurtuba Road
info@heron-provisions.example
www.heron-provisions.example
Requirements: 1. Business card 2. Letterhead 3. Envelope (C4, C5, C6, DL) check attached image 4. Notepad
Design
adnanalawf adnanalawf
Thanks to everyone really nice work, but please don't submit business card solo, I don't need all stationery i need only what's mentioned in additional comments section in the brief.
ArtworksKingdom ArtworksKingdom
Rating star please..
Thanks, What about the other stationery.

```html
<!DOCTYPE html>
<html lang="en">
<head>
<meta charset="utf-8">
<title>Heron Provisions – Business Card</title>
<link rel="stylesheet" href="https://fonts.googleapis.com/css2?family=Cinzel:wght@400;600&family=Crimson+Text:wght@400&display=swap">
<style>
  :root {
    --bg: #8f9296;
    --card-blue: #3b78c3;
    --card-blue-dark: #2f63a8;
    --card-white: #ffffff;
    --ink-blue: #2c5ea8;
    --ink-dark: #3a4660;
    --shadow: rgba(0, 0, 0, 0.28);
  }
  * { margin: 0; padding: 0; box-sizing: border-box; }
  html, body {
    width: 1200px; height: 908px; overflow: hidden;
    background: var(--bg);
  }
  .stage {
    width: 1200px; height: 908px;
    display: flex; flex-direction: column;
    align-items: center; justify-content: center; gap: 40px;
  }
  .card {
    width: 700px; height: 400px;
    border-radius: 26px;
    box-shadow: 0 10px 28px var(--shadow);
    position: relative; overflow: hidden;
  }
  .card--front {
    background: linear-gradient(135deg, var(--card-blue) 0%, var(--card-blue-dark) 100%);
    display: flex; align-items: center; justify-content: center;
  }
  .brand-disc {
    width: 210px; height: 210px; border-radius: 50%;
    background: var(--card-white);
    display: flex; align-items: center; justify-content: center;
    text-align: center;
  }
  .brand-name {
    font-family: "Cinzel", serif; font-weight: 600;
    color: var(--ink-blue); font-size: 24px; line-height: 1.25;
    letter-spacing: 1px;
  }
  .card--back { background: var(--card-white); }
  .back-brand {
    position: absolute; left: 46px; top: 48px; width: 200px;
    font-family: "Cinzel", serif; font-weight: 600;
    color: var(--ink-blue); font-size: 24px; line-height: 1.25;
    letter-spacing: 1px;
  }
  .contact-list {
    position: absolute; left: 300px; top: 44px; right: 40px;
    list-style: none;
    font-family: "Crimson Text", serif; font-size: 17px; line-height: 1;
    color: var(--ink-dark);
  }
  .contact-list li {
    display: flex; align-items: center; gap: 10px;
    height: 30px; white-space: nowrap;
  }
  .contact-list li.gap { margin-top: 8px; }
  .contact-icon { width: 18px; height: 18px; flex: none; }
  .contact-icon--blank { visibility: hidden; }
  .person {
    position: absolute; left: 46px; bottom: 44px;
    font-family: "Cinzel", serif; color: var(--ink-blue);
  }
  .person-name { font-size: 26px; font-weight: 600; letter-spacing: 1px; line-height: 1.2; }
  .person-title { font-size: 18px; font-weight: 400; letter-spacing: 2px; margin-top: 4px; line-height: 1.2; }
</style>
</head>
<body>
<main class="stage">
  <section class="card card--front" aria-label="Business card front">
    <div class="brand-disc">
      <span class="brand-name">Heron<br>Provisions</span>
    </div>
  </section>

  <section class="card card--back" aria-label="Business card back">
    <div class="back-brand">Heron<br>Provisions</div>

    <ul class="contact-list">
      <li>
        <svg class="contact-icon" viewBox="0 0 20 20"><circle cx="10" cy="10" r="9" fill="none" stroke="#2c5ea8" stroke-width="1.4"/><path d="M7 5.5l1.6 2.4-1 1c.6 1.3 1.5 2.2 2.8 2.8l1-1 2.4 1.6-.9 1.7c-3.4-.3-6.5-3.4-6.8-6.8z" fill="#2c5ea8"/></svg>
        <span>012 4738205</span>
      </li>
      <li>
        <svg class="contact-icon" viewBox="0 0 20 20"><circle cx="10" cy="10" r="9" fill="none" stroke="#2c5ea8" stroke-width="1.4"/><path d="M7 5.5l1.6 2.4-1 1c.6 1.3 1.5 2.2 2.8 2.8l1-1 2.4 1.6-.9 1.7c-3.4-.3-6.5-3.4-6.8-6.8z" fill="#2c5ea8"/></svg>
        <span>012 4719360</span>
      </li>
      <li>
        <svg class="contact-icon" viewBox="0 0 20 20"><circle cx="10" cy="10" r="9" fill="none" stroke="#2c5ea8" stroke-width="1.4"/><rect x="5.5" y="8" width="9" height="6" rx="1" fill="#2c5ea8"/><rect x="7" y="5" width="6" height="3" fill="none" stroke="#2c5ea8" stroke-width="1.2"/></svg>
        <span>012 4782513</span>
      </li>
      <li class="gap">
        <svg class="contact-icon" viewBox="0 0 20 20"><circle cx="10" cy="10" r="9" fill="none" stroke="#2c5ea8" stroke-width="1.4"/><path d="M10 4.5a3.5 3.5 0 0 0-3.5 3.5c0 2.6 3.5 7 3.5 7s3.5-4.4 3.5-7A3.5 3.5 0 0 0 10 4.5z" fill="#2c5ea8"/><circle cx="10" cy="8" r="1.3" fill="#fff"/></svg>
        <span>487 Jeddah 23857</span>
      </li>
      <li>
        <svg class="contact-icon contact-icon--blank" viewBox="0 0 20 20"></svg>
        <span>Sawsan St. Sawsan cross Qurtuba Road</span>
      </li>
      <li class="gap">
        <svg class="contact-icon" viewBox="0 0 20 20"><circle cx="10" cy="10" r="9" fill="none" stroke="#2c5ea8" stroke-width="1.4"/><rect x="5" y="6.5" width="10" height="7" rx="1" fill="none" stroke="#2c5ea8" stroke-width="1.3"/><path d="M5.3 7l4.7 3.6L14.7 7" fill="none" stroke="#2c5ea8" stroke-width="1.3"/></svg>
        <span>info@heron-provisions.example</span>
      </li>
      <li>
        <svg class="contact-icon" viewBox="0 0 20 20"><circle cx="10" cy="10" r="9" fill="none" stroke="#2c5ea8" stroke-width="1.4"/><circle cx="10" cy="10" r="5" fill="none" stroke="#2c5ea8" stroke-width="1.2"/><path d="M5 10h10M10 5c-2 3-2 7 0 10M10 5c2 3 2 7 0 10" fill="none" stroke="#2c5ea8" stroke-width="1.1"/></svg>
        <span>www.heron-provisions.example</span>
      </li>
    </ul>

    <div class="person">
      <div class="person-name">Faisal Bakrouni</div>
      <div class="person-title">CEO</div>
    </div>
  </section>
</main>
</body>
</html>
```